New Sports Team- Womens Football

New team in San Diego.  Looking for a website that can be updated by us after the design is established.
Pages needed:
About us
Roster
Coaches/Staff
Schedule
Online Store (This link will go out to an external vendor)
Community Partners /Sponsors
Some good team pages to take a look at:
lakeportkestrels.example
brimfieldtidewatchfootball.example

Please use the logo I attempted to upload.  Looking for Flash Intro that incorporates the definition of the word "VANTA" and then the logo appearing.
Use the following words:
;any sudden, strong increase, as of energy, enthusiasm, etc.
;To improve one's performance suddenly, especially in bettering one's standing in a competition.

I placed a couple more pictures.
Adding another version of the team logo. In all designs I have seen thus far, everyone has the logo very small and it appears transparent. Might help to have the jpeg version. Also added some more photos
We are approaching the deadline quickly. Just a few last notes to the designs I have been viewing. All designs that are not close to the brief will be eliminated.

```html
<!DOCTYPE html>
<html lang="en">
<head>
<meta charset="utf-8">
<title>VANTA Women's Football</title>
<link href="https://fonts.googleapis.com/css2?family=Arimo:wght@400;700&display=swap" rel="stylesheet">
<style>
:root{
  --page:#0e2452;
  --topbar:#050505;
  --blue:#1660cf;
  --blue-dark:#0a45a8;
  --blue-light:#3d8fe0;
  --panel:#141414;
  --panel-mid:#2c2c2c;
  --panel-row:#232323;
  --ink:#1c1c1c;
  --muted:#9a9a9a;
  --white:#ffffff;
  --link:#1f4fae;
}
*{box-sizing:border-box;margin:0;padding:0}
html,body{width:873px;height:1200px;overflow:hidden}
body{background:var(--page);font-family:"Arimo",Arial,sans-serif;color:var(--white);position:relative}
.abs{position:absolute}

.topbar{left:0;top:0;width:873px;height:21px;background:var(--topbar);font-size:9px;display:flex;gap:8px;align-items:center;justify-content:flex-end;padding-right:100px}
.topbar b{font-weight:700}

.header{left:92px;top:37px;width:703px;height:138px;background:var(--white);border-radius:11px;overflow:hidden;border:2px solid var(--blue-dark)}
.brand-band{left:0;top:0;width:100%;height:87px;background:linear-gradient(90deg,#f3f8fd 0%,#9cc6ee 14%,#2b82d8 40%,#1167c6 100%)}
.brand{left:62px;top:26px;font-size:34px;font-weight:700;color:var(--white);letter-spacing:1px;display:flex;align-items:center;gap:8px}
.brand .dot{width:16px;height:16px;border-radius:50%;background:var(--white)}
.callus{right:10px;top:13px;font-size:17px}
.social{right:4px;top:58px;display:flex;gap:4px}
.social span{width:24px;height:24px;border-radius:5px;background:#e8eef6;border:1px solid #9fb8d8}
.nav{left:0;top:85px;width:100%;height:30px;background:var(--blue-dark);display:flex;gap:3px;padding-top:1px}
.nav a{display:flex;align-items:center;justify-content:center;width:74px;height:28px;background:linear-gradient(#5a5a5a,#262626);color:var(--white);font-size:10px;font-weight:700;text-decoration:none;text-transform:uppercase}
.nav a.active{width:83px;background:linear-gradient(var(--blue-light),var(--blue))}
.header-foot{left:0;top:115px;width:100%;height:23px;background:var(--white)}

.slider{left:92px;top:191px;width:703px;height:340px;background:var(--panel);border-radius:12px}
.feature{left:9px;top:10px;width:415px;height:318px;background:linear-gradient(180deg,#9a8f78 0%,#6c6a4e 45%,#3f5a2c 75%,#2e4a22 100%)}
.feature-caption{left:9px;top:242px;width:415px;height:76px;background:rgba(42,42,42,.94);padding:20px 0 0 22px}
.feature-caption h2{font-size:11.5px;font-weight:700;white-space:nowrap}
.feature-caption p{font-size:8px;margin-top:15px}
.play{right:20px;top:42px}
.stories{left:436px;top:10px;width:265px}
.story{display:flex;height:77px;margin-bottom:3px;background:#3a3a3a}
.story-text{width:149px;padding:17px 0 0 18px;font-size:8.5px;font-weight:700;line-height:11.5px;background:linear-gradient(90deg,#2c2c2c,#444)}
.story-photo{width:116px}

.box-title{font-size:13px;font-weight:700;color:var(--ink);height:22px}
.see-all{display:block;font-size:9px;font-weight:700;color:var(--ink);text-decoration:underline}

.side-left{left:92px;top:541px;width:148px}
.contact{height:199px;background:linear-gradient(#fff 0%,#f2f2f2 40%,#bdbdbd 100%);border-radius:9px 0 0 0;padding:11px 13px;color:var(--ink)}
.contact .field{width:125px;height:15px;border:1px solid #9a9a9a;background:#fff;font-size:7px;color:#888;padding:2px 3px;margin-top:3px}
.contact .first{margin-top:7px}
.contact .message{height:64px}
.buttons{display:flex;gap:6px;margin:8px 0 0 12px}
.buttons span{background:linear-gradient(var(--blue-light),var(--blue-dark));color:#fff;font-size:8px;padding:3px 8px;border:1px solid #0a3a8a}
.articles{height:247px;background:linear-gradient(#fff 0%,#eee 60%,#b8b8b8 100%);border-radius:0 0 0 10px;padding:12px 13px;color:var(--ink);margin-top:1px}
.article{height:57px;padding-top:14px;border-bottom:1px solid #aaa;font-size:7.6px;line-height:11px;overflow:hidden}
.article b{font-size:8px;display:block}
.articles .see-all{margin-top:15px}

.main{left:244px;top:541px;width:399px;height:599px;background:var(--panel-mid)}
.tabs{height:22px;background:#111;display:flex;font-size:10px;font-weight:700;color:#bbb}
.tabs span{padding:5px 10px 0}
.tabs .active{background:var(--panel-row);color:#fff}
.headlines{height:176px;background:#222;padding:17px 11px}
.headline{display:flex;height:27px;border-bottom:1px solid #333;align-items:center;font-size:8px;font-weight:700;background:#161616;white-space:nowrap}
.headline .date{width:80px;height:100%;display:flex;align-items:center;justify-content:center;background:#1b1b1b;color:#666;font-size:7px;font-weight:400;margin-right:10px}
.topics{padding:17px 11px 0}
.topics h3{font-size:14px;font-weight:700}
.topic{padding:16px 0 14px;border-bottom:1px solid #888}
.topic h4{font-size:11px;font-weight:700;line-height:13px}
.topic-body{display:flex;gap:9px;margin-top:9px}
.topic-photo{width:185px;height:117px;flex:none}
.topic-body p{font-size:7.8px;color:var(--muted);line-height:12px;padding-top:2px}

.side-right{left:647px;top:541px;width:148px;height:606px;background:linear-gradient(#fff 0%,#f0f0f0 45%,#b5b5b5 100%);border-radius:10px 10px 0 0;padding:10px 13px;color:var(--ink)}
.side-right .box-title{font-size:15px;height:32px}
.news{height:136px;border-bottom:1px solid #aaa;overflow:hidden}
.news b{font-size:8px;display:block}
.news-photo{width:121px;height:60px;margin:8px 0 20px}
.news p{font-size:7.6px;line-height:12px}
.side-right .see-all{text-align:right;margin-top:5px}

.footer-nav{left:109px;top:1153px;display:flex;gap:10px;font-size:10.5px}
.footer-nav a{color:var(--link);text-decoration:none;text-transform:uppercase}
.copyright{left:0;top:1182px;width:873px;text-align:center;font-size:8.5px}
</style>
</head>
<body>

<div class="abs topbar"><b>New User?</b><span>Register</span><span>Sign In</span><span>Help</span></div>

<header class="abs header">
  <div class="abs brand-band"></div>
  <div class="abs brand"><span class="dot"></span>VANTA</div>
  <div class="abs callus">CALL US:555.014.027</div>
  <div class="abs social"><span></span><span></span><span></span></div>
  <nav class="abs nav">
    <a class="active">About us</a><a>Roster</a><a>Staff</a><a>Schedule</a><a>Online</a><a>Store</a><a>Community</a><a>Sponsors</a>
  </nav>
  <div class="abs header-foot"></div>
</header>

<section class="abs slider">
  <div class="abs feature" role="img" aria-label="Team photo of players flexing on a grass field at dusk"></div>
  <div class="abs feature-caption">
    <h2>Lorem Ipsum is simply dummy text of the printing and&nbsp; industry.</h2>
    <p>Lorem Ipsum is simply dummy text of the printing and typesetting industry.</p>
    <svg class="abs play" width="20" height="20" viewBox="0 0 20 20"><circle cx="10" cy="10" r="8.5" fill="none" stroke="#fff" stroke-width="1.5"/><path d="M8 6.5l5 3.5-5 3.5z" fill="#fff"/></svg>
  </div>
  <div class="abs stories">
    <div class="story"><div class="story-text">SEP 10,2010<br>It is a long established fact that a reader will be distracted by the .</div><div class="story-photo" role="img" aria-label="Players in maroon and yellow during a match" style="background:linear-gradient(#c9b9a6,#7a4452 50%,#4f7a3a)"></div></div>
    <div class="story"><div class="story-text">SEP 10,2010<br>It is a long established fact that a reader will be distracted by the .</div><div class="story-photo" role="img" aria-label="Two players in navy and gold jerseys" style="background:linear-gradient(#3f5fae,#2b3f80 40%,#d1a830)"></div></div>
    <div class="story"><div class="story-text">SEP 10,2010<br>It is a long established fact that a reader will be distracted by the .</div><div class="story-photo" role="img" aria-label="Group of players posing together" style="background:linear-gradient(#e9e4dc,#b48a78 50%,#7d2b3a)"></div></div>
    <div class="story"><div class="story-text">SEP 10,2010<br>It is a long established fact that a reader will be distracted by the .</div><div class="story-photo" role="img" aria-label="Full squad team photo in orange kit" style="background:linear-gradient(#c9c6b5,#d88a2a 50%,#5d7a36)"></div></div>
  </div>
</section>

<aside class="abs side-left">
  <div class="contact">
    <div class="box-title">CONTACT US</div>
    <div class="field first">Name</div>
    <div class="field">Email</div>
    <div class="field">Phone</div>
    <div class="field message">Message</div>
    <div class="buttons"><span>Sumit</span><span>Clear</span></div>
  </div>
  <div class="articles">
    <div class="box-title">LATEST ARTICLES</div>
    <div class="article"><b>SEP 10,2010</b>It is a long established fact that<br>a reader will be distracted by the</div>
    <div class="article"><b>SEP 10,2010</b>It is a long established fact that<br>a reader will be distracted by the</div>
    <div class="article"><b>SEP 10,2010</b>It is a long established fact that<br>a reader will be distracted by the</div>
    <a class="see-all">See all</a>
  </div>
</aside>

<main class="abs main">
  <div class="tabs"><span class="active">HEADLINES</span><span>FULL SCHEDULE</span><span>APPEARANCES</span></div>
  <div class="headlines">
    <div class="headline"><span class="date">SEP 10,2010</span>Lorem Ipsum is simply dummy text of the printing and&nbsp; industry.</div>
    <div class="headline"><span class="date">SEP 10,2010</span>Lorem Ipsum is simply dummy text of the printing and&nbsp; industry.</div>
    <div class="headline"><span class="date">SEP 10,2010</span>Lorem Ipsum is simply dummy text of the printing and&nbsp; industry.</div>
    <div class="headline"><span class="date">SEP 10,2010</span>Lorem Ipsum is simply dummy text of the printing and&nbsp; industry.</div>
    <div class="headline"><span class="date">SEP 10,2010</span>Lorem Ipsum is simply dummy text of the printing and&nbsp; industry.</div>
  </div>
  <div class="topics">
    <h3>LATEST TOPICS</h3>
    <div class="topic">
      <h4>Lorem Ipsum is simply dummy text of the printing<br>and typesetting industry.</h4>
      <div class="topic-body">
        <div class="topic-photo" role="img" aria-label="Rugby tackle between red-black and white teams" style="background:linear-gradient(#8a9a8c,#6a3a36 45%,#5e8a3c)"></div>
        <p>Lorem Ipsum is simply dummy text of the printing and typesetting industry. Lorem Ipsum has been the industry's standard dummy text ever since the 1500s, Ipsum has been the iLorem Ipsum is simply dummy text of the printing and typesetting industry. Lorem Ipsum has been the industry's standard dummy text ever since</p>
      </div>
    </div>
    <div class="topic">
      <h4>Lorem Ipsum is simply dummy text of the printing<br>and typesetting industry.</h4>
      <div class="topic-body">
        <div class="topic-photo" role="img" aria-label="Players in navy and white contesting the ball" style="background:linear-gradient(#2e3c78,#5a5f86 45%,#cfd2da 70%,#4d7a34)"></div>
        <p>Lorem Ipsum is simply dummy text of the printing and typesetting industry. Lorem Ipsum has been the industry's standard dummy text ever since the 1500s, Ipsum has been the iLorem Ipsum is simply dummy text of the printing and typesetting industry. Lorem Ipsum has been the industry's standard dummy text ever since</p>
      </div>
    </div>
  </div>
</main>

<aside class="abs side-right">
  <div class="box-title">LATEST NEWS</div>
  <div class="news"><b>SEP 10,2010</b><div class="news-photo" role="img" aria-label="Players running with the ball" style="background:linear-gradient(#8a8f98,#4b5060 50%,#6a8a4c)"></div><p>It is a long established fact that<br>a reader will be distracted by the</p></div>
  <div class="news"><b>SEP 10,2010</b><div class="news-photo" role="img" aria-label="Match action on a green field" style="background:linear-gradient(#6d8a54,#9a2e2e 50%,#4e7a36)"></div><p>It is a long established fact that<br>a reader will be distracted by the</p></div>
  <div class="news"><b>SEP 10,2010</b><div class="news-photo" role="img" aria-label="Players lined up wearing medals" style="background:linear-gradient(#2a2f52,#5a4a6a 50%,#8a7a8a)"></div><p>It is a long established fact that<br>a reader will be distracted by the</p></div>
  <div class="news"><b>SEP 10,2010</b><div class="news-photo" role="img" aria-label="Team group photo on grass" style="background:linear-gradient(#c8d4c0,#2a2a2a 50%,#5e8a3a)"></div><p>It is a long established fact that<br>a reader will be distracted by the</p></div>
  <a class="see-all">See all</a>
</aside>

<nav class="abs footer-nav"><a>About us</a><a>Roster</a><a>Staff</a><a>Schedule</a><a>Online</a><a>Store</a><a>Community</a><a>Sponsors</a></nav>
<div class="abs copyright">Copyright © 2010 VANTA woman football .</div>

</body>
</html>
```